Morvek Menu

Hi there,
My restaurant called "Morvek" means Spice in hebrew.
We are middle eastern restaurant that specialist in dips,salads and hot bread baked on the spot and charcoal grilled meat skewers
The restaurant is pretty casual and the atmosphere is nice and customers feels like home.
on www.morvek.com.au you can see photos of the restaurant and the food.
ill add up the menus that i would like to be design please and the logo that is on the front of the shop is been add up
thank you

Target Market(s)

The regulars of the restaurant is jewish/israelis

Industry/Entity Type

Restaurant

```html
<!DOCTYPE html>
<html lang="en">
<head>
<meta charset="utf-8">
<title>Morvek Dinner &amp; Take Away Menu</title>
<link href="https://fonts.googleapis.com/css2?family=Raleway:wght@300;400;600&family=Open+Sans:wght@400;600&display=swap" rel="stylesheet">
<style>
:root{
  --bg:#e4e4e4;
  --paper:#ffffff;
  --ink:#4a4a4a;
  --ink-soft:#8a8a8a;
  --rule:#7a7a7a;
  --accent:#c2404c;
  --marker:#e3b04b;
  --band:#1c1c1c;
  --cover-light:#f4f4f4;
  --cover-mid:#d9d9d9;
}
*{box-sizing:border-box;margin:0;padding:0}
html,body{width:1200px;height:800px;overflow:hidden}
body{background:var(--bg);font-family:"Open Sans",Arial,sans-serif;color:var(--ink);position:relative}
.sheet{position:absolute;top:140px;left:32px;display:flex;gap:32px}
.spread{display:flex;box-shadow:0 6px 20px rgba(0,0,0,.15)}
.page{width:368px;height:520px;background:var(--paper);padding:22px 22px 18px;position:relative}
.page + .page{border-left:1px solid #e2e2e2}
.menu-head{display:flex;justify-content:space-between;align-items:flex-end;border-bottom:1px solid var(--rule);padding-bottom:4px}
.menu-title{font-family:"Raleway",Arial,sans-serif;font-weight:300;font-size:25px;letter-spacing:5px;color:#333}
.contact{font-size:6px;line-height:1.35;color:var(--ink-soft);border-left:1px solid var(--rule);padding-left:5px;text-align:left}
.dots{display:flex;justify-content:space-between;padding:3px 10px 0;font-size:6px;color:var(--ink-soft);letter-spacing:2px}
.section{margin-top:7px}
.section-title{display:flex;align-items:center;gap:4px;color:var(--accent);font-size:8px;font-weight:600;border-bottom:1px solid #bbb;padding-bottom:1px;margin-bottom:2px}
.section-title::before{content:"";width:4px;height:4px;background:var(--marker)}
.section-note{font-size:5.5px;color:var(--ink-soft);font-weight:400;margin-left:6px}
.items{display:grid;grid-template-columns:1fr 1fr;column-gap:16px}
.items.single{grid-template-columns:1fr}
.item{display:flex;justify-content:space-between;font-size:6.5px;line-height:1.45}
.item span:last-child{color:var(--ink-soft)}
.footnote{position:absolute;left:22px;right:22px;bottom:20px;font-size:6px;color:var(--ink-soft);text-align:center;line-height:1.5}
.cover{width:368px;height:520px;position:relative;overflow:hidden;background:linear-gradient(160deg,var(--cover-light),var(--cover-mid));box-shadow:0 6px 20px rgba(0,0,0,.15)}
.cover-ornament{position:absolute;left:60px;top:150px;width:240px;height:240px;border-radius:50%;background:radial-gradient(circle,rgba(255,255,255,.7),rgba(255,255,255,0) 70%)}
.cover-band{position:absolute;top:0;bottom:0;left:112px;width:96px;background:var(--band)}
.brand{position:absolute;top:22px;left:112px;width:96px;display:flex;flex-direction:column;align-items:center;gap:4px;color:#fff;font-family:"Raleway",Arial,sans-serif;font-size:14px;font-weight:400}
.brand-mark{width:10px;height:10px;background:#fff}
.cover-plate{position:absolute;left:60px;top:170px;width:200px;height:200px}
.cover-title{position:absolute;left:60px;top:200px;width:200px;text-align:center;color:#fff;font-family:"Raleway",Arial,sans-serif;font-weight:300;font-size:17px;line-height:1.3}
.cover-title .big{font-size:26px;letter-spacing:3px;display:block;margin-top:6px}
.cover-address{position:absolute;bottom:26px;left:112px;width:90px;text-align:right;color:#fff;font-size:6.5px;line-height:1.5}
</style>
</head>
<body>
<main class="sheet">
  <div class="spread">
    <section class="page dinner">
      <header class="menu-head">
        <h1 class="menu-title">Dinner Menu</h1>
        <p class="contact">214 Harlow Road<br>Elmwood South<br>Tel. 9481 3720</p>
      </header>
      <div class="dots"><span>•</span><span>•</span><span>•</span><span>•</span><span>•</span><span>•</span><span>•</span></div>

      <div class="section"><h2 class="section-title">Something to start with</h2>
        <div class="items"><p class="item"><span>Bread &amp; Dips</span><span>$5</span></p><p class="item"><span>Fried Cauliflower</span><span>$7</span></p><p class="item"><span>5 Falafel Balls</span><span>$6.50</span></p><p class="item"><span>Moroccan Beef Cigars</span><span>$9</span></p></div></div>

      <div class="section"><h2 class="section-title">Salads &amp; Dips</h2>
        <div class="items"><p class="item"><span>Hummus</span><span>$8.50</span></p><p class="item"><span>Moroccan Carrot</span><span>$7.50</span></p><p class="item"><span>Baba Ghanoush</span><span>$8</span></p><p class="item"><span>Roasted Beetroot</span><span>$7</span></p><p class="item"><span>Matbucha Tomato Salsa</span><span>$7</span></p><p class="item"><span>Tahini</span><span>$6</span></p></div></div>

      <div class="section"><h2 class="section-title">From the charcoal grill <span class="section-note">served with chips and salad</span></h2>
        <div class="items"><p class="item"><span>Chicken Shashlik</span><span>$24</span></p><p class="item"><span>Kebab Beef Shashlik</span><span>$26</span></p><p class="item"><span>Lamb Shashlik</span><span>$28</span></p><p class="item"><span>Chicken Liver</span><span>$22</span></p></div></div>

      <div class="section"><h2 class="section-title">Hummus Plates</h2>
        <div class="items"><p class="item"><span>Mashawsha</span><span>$15</span></p><p class="item"><span>Mushroom</span><span>$16</span></p><p class="item"><span>Ful</span><span>$15</span></p><p class="item"><span>Beef</span><span>$18</span></p></div></div>

      <div class="section"><h2 class="section-title">Sides</h2>
        <div class="items"><p class="item"><span>Chips</span><span>$6</span></p><p class="item"><span>Israeli Salad</span><span>$8</span></p></div></div>

      <div class="section"><h2 class="section-title">Desserts</h2>
        <div class="items"><p class="item"><span>Malabi</span><span>$9</span></p><p class="item"><span>Semolina Cake</span><span>$9</span></p><p class="item"><span>Trio of Sorbet</span><span>$10</span></p><p class="item"><span>Turkish Delight Ice-cream</span><span>$11</span></p></div></div>

      <div class="section"><h2 class="section-title">Plates</h2>
        <div class="items"><p class="item"><span>Falafel</span><span>$18.5</span></p><p class="item"><span>Kofta</span><span>$22</span></p><p class="item"><span>Schnitzel</span><span>$21</span></p><p class="item"><span>Lamb</span><span>$25</span></p></div></div>

      <div class="section"><h2 class="section-title">Kids (10 and under only)</h2>
        <div class="items"><p class="item"><span>Schnitzel Plate with salad and chips</span><span>$10</span></p><p class="item"><span>Falafel Plate with salad and chips</span><span>$9</span></p></div></div>

      <div class="section"><h2 class="section-title">Drinks</h2>
        <div class="items"><p class="item"><span>Cola/Diet Cola/Orange Soda/Lemon Soda</span><span>$3.5</span></p><p class="item"><span>Coffee/Chai/Hot Chocolate</span><span>$4</span></p><p class="item"><span>Sparkling/Mineral Water</span><span>$4</span></p><p class="item"><span>Turkish Coffee</span><span>$4.5</span></p><p class="item"><span>Lemonana with fresh mint</span><span>$5</span></p><p class="item"><span>Israeli Grape/Strawberry Banana</span><span>$6</span></p></div></div>
    </section>

    <section class="page takeaway">
      <header class="menu-head">
        <h1 class="menu-title">Take Away Menu</h1>
        <p class="contact">214 Harlow Road<br>Elmwood South<br>Tel. 9481 3720</p>
      </header>
      <div class="dots"><span>•</span><span>•</span><span>•</span><span>•</span><span>•</span><span>•</span><span>•</span></div>

      <div class="section"><h2 class="section-title">Salads &amp; Dips <span class="section-note">small $5.90 / large $9.90</span></h2>
        <div class="items"><p class="item"><span>Hummus (GF)</span><span>$5.90</span></p><p class="item"><span>Moroccan Carrot (GF)</span><span>$5.90</span></p><p class="item"><span>Baba Ghanoush (GF)</span><span>$5.90</span></p><p class="item"><span>Roasted Beetroot (GF)</span><span>$5.90</span></p><p class="item"><span>Matbucha (GF)</span><span>$5.90</span></p><p class="item"><span>Tahini (GF)</span><span>$5.90</span></p></div></div>

      <div class="section"><h2 class="section-title">Hummus Plates <span class="section-note">served with pita and pickles</span></h2>
        <div class="items single"><p class="item"><span>Mashawsha — warm chickpeas, tahini and lemon</span><span>$14.90</span></p><p class="item"><span>Mushroom — sautéed with onion and herbs</span><span>$15.90</span></p><p class="item"><span>Beef — spiced mince with pine nuts</span><span>$17.90</span></p></div></div>

      <div class="section"><h2 class="section-title">Lafa Wraps</h2>
        <div class="items"><p class="item"><span>Falafel</span><span>$12</span></p><p class="item"><span>Kofta</span><span>$15</span></p><p class="item"><span>Chicken Shashlik</span><span>$15</span></p><p class="item"><span>Lamb Shashlik</span><span>$17</span></p><p class="item"><span>Schnitzel</span><span>$14</span></p></div></div>

      <div class="section"><h2 class="section-title">From the charcoal grill</h2>
        <div class="items single"><p class="item"><span>Chicken Shashlik</span><span>$8.50 (GF)</span></p><p class="item"><span>Kebab Beef Shashlik</span><span>$9.50 (GF)</span></p><p class="item"><span>Lamb Shashlik</span><span>$10.50 (GF)</span></p></div></div>

      <div class="section"><h2 class="section-title">Sides</h2>
        <div class="items"><p class="item"><span>Chips</span><span>$6</span></p><p class="item"><span>Moroccan Beef Cigars</span><span>$9</span></p><p class="item"><span>Falafel Balls (6 per serve)</span><span>$8</span></p><p class="item"><span>Lafa</span><span>$3</span></p></div></div>

      <p class="footnote">Morvek is able to provide catering for your dinner parties and events. For more information please contact us.<br>Prices subject to change without notice.</p>
    </section>
  </div>

  <section class="cover">
    <div class="cover-ornament" role="img" aria-label="Faint large star ornament behind the cover title"></div>
    <div class="cover-band"></div>
    <div class="brand"><span>Morvek</span><span class="brand-mark"></span></div>
    <svg class="cover-plate" viewBox="0 0 200 200" aria-hidden="true">
      <polygon points="100,0 187,50 187,150 100,200 13,150 13,50" fill="#1c1c1c"/>
    </svg>
    <h2 class="cover-title">Dinner<br>&amp;<br>Take Away<span class="big">MENU</span></h2>
    <p class="cover-address">214 Harlow Road,<br>Elmwood South<br>Tel. 9481 3720</p>
  </section>
</main>
</body>
</html>
```